Business Cards and Stationery incorporating Logo design
Business Cards and Stationery incorporating Logo design -
Creative Brief
Professional
Daniel P. Halvorsen
Managing Director
418 Corvane Tower 9th Fl. Brookhaven Falls, OH 44021
1-555-hdg-cash
dhalvorsen@halvorsendrakeco.example
www.halvorsendrakeco.example

```html
<!DOCTYPE html>
<html lang="en">
<head>
<meta charset="utf-8">
<title>Halvorsen Drake — Business Card</title>
<link rel="stylesheet" href="https://fonts.googleapis.com/css2?family=Cinzel:wght@500;600&family=Open+Sans:ital,wght@1,600;1,700&family=Tinos&display=swap">
<style>
  :root {
    --backdrop: #3a3a3a;
    --card: #ffffff;
    --brand-green: #1c7a3e;
    --brand-green-dark: #145c2e;
    --ink: #1d1d1d;
    --muted-ink: #333333;
    --faint-mark: #e8ece9;
  }
  html, body {
    margin: 0;
    padding: 0;
    width: 1200px;
    height: 780px;
    overflow: hidden;
    background: var(--backdrop);
  }
  .card {
    position: absolute;
    left: 100px;
    top: 105px;
    width: 1000px;
    height: 570px;
    background: var(--card);
    border-radius: 28px;
    overflow: hidden;
  }
  .side-band {
    position: absolute;
    left: 0;
    top: 150px;
    width: 165px;
    height: 420px;
    background: var(--brand-green);
  }
  .brand-square {
    position: absolute;
    left: 115px;
    top: 120px;
    width: 110px;
    height: 110px;
    background: var(--brand-green-dark);
    border: 5px solid var(--card);
  }
  .brand-rule {
    position: absolute;
    left: 252px;
    top: 70px;
    width: 3px;
    height: 470px;
    background: var(--ink);
  }
  .wordmark {
    position: absolute;
    left: 272px;
    top: 66px;
    font-family: "Cinzel", serif;
    font-weight: 600;
    font-size: 56px;
    line-height: 60px;
    color: var(--brand-green);
    letter-spacing: 1px;
  }
  .faint-mark {
    position: absolute;
    left: 700px;
    top: 200px;
    width: 230px;
    height: 230px;
    background: var(--faint-mark);
  }
  .contact {
    position: absolute;
    left: 272px;
    top: 222px;
  }
  .person-name {
    font-family: "Open Sans", sans-serif;
    font-style: italic;
    font-weight: 700;
    font-size: 25px;
    line-height: 32px;
    color: var(--brand-green);
    margin: 0;
  }
  .person-title {
    font-family: "Open Sans", sans-serif;
    font-style: italic;
    font-weight: 600;
    font-size: 18px;
    line-height: 24px;
    color: var(--muted-ink);
    margin: 0 0 18px;
  }
  .detail {
    display: flex;
    align-items: flex-start;
    gap: 12px;
    font-family: "Tinos", serif;
    font-size: 20px;
    line-height: 25px;
    color: var(--muted-ink);
    margin-bottom: 7px;
  }
  .detail svg {
    flex: none;
    width: 19px;
    height: 19px;
    margin-top: 3px;
    fill: var(--brand-green);
  }
  .detail .at {
    flex: none;
    width: 19px;
    color: var(--brand-green);
    font-weight: bold;
  }
</style>
</head>
<body>
  <div class="card">
    <div class="side-band"></div>
    <div class="brand-square"></div>
    <div class="brand-rule"></div>
    <div class="wordmark">Halvorsen<br>Drake</div>
    <div class="faint-mark"></div>

    <div class="contact">
      <p class="person-name">Daniel P. Halvorsen</p>
      <p class="person-title">Managing Director</p>

      <div class="detail">
        <svg viewBox="0 0 20 20"><path d="M10 2 L19 10 H16 V18 H12 V13 H8 V18 H4 V10 H1 Z"/></svg>
        <span>418 Corvane Tower<br>9th Fl. Brookhaven Falls, OH 44021</span>
      </div>
      <div class="detail">
        <svg viewBox="0 0 20 20"><path d="M5 2 L8 6 L6 8 C7 11 9 13 12 14 L14 12 L18 15 L16 18 C9 18 2 11 2 4 Z"/></svg>
        <span>1-555-hdg-cash</span>
      </div>
      <div class="detail">
        <svg viewBox="0 0 20 20"><path d="M5 2 L8 6 L6 8 C7 11 9 13 12 14 L14 12 L18 15 L16 18 C9 18 2 11 2 4 Z"/></svg>
        <span>(555) 310-4827</span>
      </div>
      <div class="detail">
        <svg viewBox="0 0 20 20"><path d="M6 1 H14 V19 H6 Z M8 3 V14 H12 V3 Z"/></svg>
        <span>(555) 672-1904</span>
      </div>
      <div class="detail">
        <span class="at">@</span>
        <span>dhalvorsen@halvorsendrakeco.example</span>
      </div>
    </div>
  </div>
</body>
</html>
```